Feminine colorfull packaging for coconut skin care brand

We need a design that can be used on different types of packaging for beauty products likes creams, oils, etc.
The products that we will launch will be made with one key ingredient of coconut oil + other added ingredients depending on the type of product. The entire marketing will therefore be based on COCONUTS, palmtrees, sand, beach, bronzing on the beach, holiday feeling, nature, femininity, etc. = A Lifestyle brand with a tropical vibe.
Packaging can be a pot for creams, flaskes for lotions, smaller bottles for oils, etc. Mostly the standard packaging used for beauty products.
We would like to use the color pink ( this can be bright or pastel or any tone of pink) to address the feminine side of our product and a tone of blue-green ( pastel, bright or any tone of this color) to accentuate the use of coconut.
Third would be the color white (this can be added through an accent somewhere on the packaging or this can be the brand name that is written in white)
Lastely we would like the packaging to be light, fresh and playfull. Please feel free to use different colors or shapes ( we do not yet have a logo. This can then be designed followed on the packaging)
The design will be printed on plastic packaging. We are open to very creative designs. We are looking for packaging that catches the eye by its design and/or colors, that is different than others, that distinguishes the product because of its packaging design.
Target Market(s)
Women between 20 - 35 years
Industry/Entity Type
Beauty
Colors
Designer to choose colors to be used in the design.
Look and feel

```html
<!DOCTYPE html>
<html lang="en">
<head>
<meta charset="utf-8">
<title>Palm Shore – Packaging Labels</title>
<link href="https://fonts.googleapis.com/css2?family=Montserrat:wght@400;500;700&display=swap" rel="stylesheet">
<style>
  :root {
    --sand: #e8e1c9;
    --label-white: #ffffff;
    --navy: #0c2f44;
    --teal: #3fb6c6;
    --leaf-blue: #3d62a3;
    --text-navy: #123a4f;
  }
  html, body {
    margin: 0;
    width: 1200px;
    height: 800px;
    overflow: hidden;
    background: var(--sand);
    font-family: "Montserrat", sans-serif;
  }
  .canvas { position: relative; width: 1200px; height: 800px; }
  .label {
    position: absolute;
    background: var(--label-white);
    box-shadow: 0 2px 10px rgba(0,0,0,0.08);
    overflow: hidden;
    color: var(--text-navy);
    text-align: center;
  }
  .leaf-band {
    position: absolute;
    left: 0;
    right: 0;
    background: linear-gradient(90deg, var(--teal), var(--leaf-blue) 45%, var(--teal));
    opacity: 0.85;
  }
  .leaf-band.top { top: 0; }
  .leaf-band.bottom { bottom: 0; }
  .brand-block {
    position: absolute;
    left: 50%;
    transform: translateX(-50%);
    background: var(--navy);
    border-radius: 6px;
  }
  .brand-name {
    position: absolute;
    left: 0; right: 0;
    color: var(--label-white);
    font-weight: 700;
    line-height: 1.05;
    text-align: center;
  }
  .product-name {
    position: absolute;
    left: 0; right: 0;
    font-weight: 500;
    letter-spacing: 0.06em;
    text-transform: uppercase;
    line-height: 1.5;
  }
  .volume { position: absolute; font-weight: 400; }

  .label-tube { left: 60px; top: 170px; width: 260px; height: 470px; }
  .label-jar { left: 350px; top: 450px; width: 330px; height: 190px; }
  .label-bottle { left: 710px; top: 170px; width: 280px; height: 470px; }
  .label-oil { left: 1020px; top: 390px; width: 130px; height: 250px; }
</style>
</head>
<body>
<main class="canvas">

  <section class="label label-tube">
    <div class="leaf-band top" style="height:48px" role="img" aria-label="Tropical palm and monstera leaf pattern"></div>
    <div class="brand-block" style="top:80px;width:170px;height:160px" role="img" aria-label="Navy brush stroke backdrop"></div>
    <div class="brand-name" style="top:128px;font-size:30px">Palm<br>Shore</div>
    <div class="product-name" style="top:278px;font-size:14px">Anti-aging<br>skin care cream</div>
    <div class="volume" style="right:60px;top:380px;font-size:11px">150ml ℮</div>
    <div class="leaf-band bottom" style="height:48px" role="img" aria-label="Tropical palm and monstera leaf pattern"></div>
  </section>

  <section class="label label-jar">
    <div class="leaf-band top" style="height:26px" role="img" aria-label="Tropical palm and monstera leaf pattern"></div>
    <div class="brand-block" style="top:48px;width:110px;height:96px" role="img" aria-label="Navy brush stroke backdrop"></div>
    <div class="brand-name" style="top:74px;font-size:20px">Palm<br>Shore</div>
    <div class="product-name" style="left:20px;right:auto;top:84px;font-size:10px;text-align:left">Hand<br>cream</div>
    <div class="volume" style="right:20px;top:92px;font-size:11px">300ml ℮</div>
    <div class="leaf-band bottom" style="height:26px" role="img" aria-label="Tropical palm and monstera leaf pattern"></div>
  </section>

  <section class="label label-bottle">
    <div class="leaf-band top" style="height:40px" role="img" aria-label="Tropical palm and monstera leaf pattern"></div>
    <div class="brand-block" style="top:70px;width:180px;height:180px" role="img" aria-label="Navy brush stroke backdrop"></div>
    <div class="brand-name" style="top:124px;font-size:34px">Palm<br>Shore</div>
    <div class="product-name" style="top:300px;font-size:16px">Gentle skin<br>cleanser</div>
    <div class="volume" style="left:40px;top:392px;font-size:17px">300ml ℮</div>
    <div class="leaf-band bottom" style="height:40px" role="img" aria-label="Tropical palm and monstera leaf pattern"></div>
  </section>

  <section class="label label-oil">
    <div class="leaf-band top" style="height:22px" role="img" aria-label="Tropical palm and monstera leaf pattern"></div>
    <div class="brand-block" style="top:36px;width:90px;height:92px" role="img" aria-label="Navy brush stroke backdrop"></div>
    <div class="brand-name" style="top:62px;font-size:17px">Palm<br>Shore</div>
    <div class="product-name" style="top:146px;font-size:9px">Skincare<br>oil</div>
    <div class="volume" style="left:0;right:0;top:200px;font-size:9px">30ml ℮</div>
    <div class="leaf-band bottom" style="height:22px" role="img" aria-label="Tropical palm and monstera leaf pattern"></div>
  </section>

</main>
</body>
</html>
```